Web Developer Wordpress theme

I'm a web developer but a poor designer so i need somebody to design me a cool and professional WordPress theme. I specialize in shopping cart developments and modifications as well as hosting for these system so would like the design to show this off. I am UK based and want this to also come across in the design.
As for colors and layout i am open mined just use your imaginantion i will let know what i think of your designs.
also forgot to mention my business name is vartelux
and my exsiting site is vartelux.co.uk

```html
<!DOCTYPE html>
<html lang="en">
<head>
<meta charset="utf-8">
<title>Vartelux – Serious Web Development</title>
<link href="https://fonts.googleapis.com/css2?family=Roboto+Condensed:wght@400;700&family=Arimo:wght@400;700&display=swap" rel="stylesheet">
<style>
:root{
  --bg:#e8e8e8;
  --orange:#f7941d;
  --blue-dark:#0e6aa0;
  --blue:#1f8fcf;
  --panel:#8ec6e4;
  --panel-edge:#a9d4ec;
  --field:#6a9fbe;
  --grey:#8e9094;
  --footer:#d6d6d6;
  --text:#555;
  --white:#fff;
}
*{box-sizing:border-box;margin:0;padding:0}
html,body{width:1200px;height:1182px;overflow:hidden}
body{position:relative;background:var(--bg);font-family:Arimo,Arial,sans-serif;color:var(--text)}
.abs{position:absolute}

.brand{left:53px;top:0;width:330px;height:116px;background:var(--white);box-shadow:0 4px 8px rgba(0,0,0,.15);display:flex;flex-direction:column;align-items:center;justify-content:center}
.brand-name{font-family:"Roboto Condensed",Arial,sans-serif;font-weight:700;font-size:52px;color:var(--orange);line-height:1}
.brand-tag{font-size:11px;letter-spacing:2px;color:#666;margin-top:6px;font-weight:700}

.social{left:985px;top:0;width:163px;height:55px;background:var(--white);border-radius:0 0 8px 8px;display:flex;gap:16px;align-items:center;justify-content:center}
.social span{width:36px;height:36px;border-radius:50%;background:#9a9a9a}
.social span:first-child{background:var(--orange)}

.nav{left:482px;top:67px;width:666px;height:50px;background:var(--grey);border-radius:7px;display:flex;justify-content:flex-end;align-items:center;gap:42px;padding-right:34px}
.nav a{color:var(--white);text-decoration:none;font-family:"Roboto Condensed",Arial,sans-serif;font-size:21px}

.sidebar{left:53px;top:147px;width:330px;height:676px;background:var(--panel);border:3px solid var(--panel-edge);border-radius:8px}
.search{position:absolute;left:20px;top:20px;width:284px;height:38px;background:var(--field);border-radius:6px;color:var(--white);font-size:13px;padding:12px 16px}
.search svg{position:absolute;right:10px;top:7px}
.ads{position:absolute;left:20px;top:72px;display:grid;grid-template-columns:136px 136px;gap:10px 12px}
.ad{width:136px;height:126px;background:#000;border:4px solid var(--white);text-align:center;color:var(--white);font-family:"Roboto Condensed",Arial,sans-serif;font-size:21px;line-height:24px;padding-top:7px}
.ad b{color:var(--orange);font-weight:700;display:block}
.ad .here{font-size:29px;line-height:31px;display:block}
.side-title{position:absolute;left:20px;font-family:"Roboto Condensed",Arial,sans-serif;font-weight:700;font-size:25px;line-height:30px;color:var(--white);width:284px;border-bottom:2px solid #4e7fa0;padding-bottom:2px}
.links{position:absolute;left:20px;top:386px;width:284px;list-style:none}
.links li{height:27px;line-height:25px;color:var(--white);font-size:16px;padding-left:26px;position:relative}
.links li::before{content:"";position:absolute;left:6px;top:8px;width:8px;height:8px;border-right:2px dotted var(--blue-dark);border-top:2px dotted var(--blue-dark);transform:rotate(45deg)}
.links li.active{background:linear-gradient(90deg,var(--orange) 40%,rgba(247,148,29,0));width:264px}
.links li.active::before{border-color:var(--white)}
.email{position:absolute;left:20px;top:568px;width:284px;height:38px;background:var(--field);border-radius:6px;color:var(--white);font-size:13px;padding:12px 16px}
.btn-round{position:absolute;height:28px;border-radius:14px;background:linear-gradient(#2a8fd0,#0d5d92);color:var(--white);font-size:12px;padding:7px 40px 0 16px;box-shadow:0 3px 3px rgba(0,0,0,.25)}
.btn-round::after{content:"";position:absolute;right:8px;top:6px;width:16px;height:16px;border-radius:50%;background:var(--white)}
.btn-round::before{content:"";position:absolute;right:14px;top:11px;border-left:6px solid var(--blue-dark);border-top:3.5px solid transparent;border-bottom:3.5px solid transparent;z-index:1}

.post{left:417px;width:731px;height:218px}
.post-title{position:absolute;left:2px;top:6px;width:470px;font-family:"Roboto Condensed",Arial,sans-serif;font-weight:400;font-size:27px;line-height:33px;color:var(--orange)}
.post-excerpt{position:absolute;left:2px;top:86px;width:555px;height:72px;overflow:hidden;font-size:11.5px;line-height:24px;letter-spacing:.35px;color:#666}
.post-thumb{position:absolute;right:0;top:0;width:150px;height:140px;border-radius:12px;border:5px solid #8d8d8d;background:linear-gradient(135deg,#dfe8f3,#5f8fc8 60%,#2a5aa0)}
.post-meta{position:absolute;left:0;top:171px;width:731px;height:45px;background:var(--panel);border-radius:7px;font-size:12px;color:var(--white);padding:15px 14px}
.post-meta em{font-style:normal;color:var(--blue-dark)}
.comments,.more{position:absolute;top:8px;height:30px;border-radius:4px;color:var(--white);font-family:"Roboto Condensed",Arial,sans-serif;font-size:17px;text-align:center;line-height:30px}
.comments{left:497px;width:115px;background:var(--blue-dark)}
.more{left:620px;width:101px;background:var(--grey)}

.footer{left:0;top:890px;width:1200px;height:255px;background:var(--footer)}
.col-title{position:absolute;top:12px;width:275px;font-family:"Roboto Condensed",Arial,sans-serif;font-weight:400;font-size:27px;color:#777;border-bottom:1px solid #bbb;padding-bottom:2px}
.blog-item{position:absolute;left:87px;width:272px;font-size:12.5px;line-height:24px;color:#555;letter-spacing:.5px;border-bottom:1px dotted #aaa;padding-bottom:6px}
.blog-item a{color:var(--blue);text-decoration:none;display:block}
.field{position:absolute;left:461px;width:276px;height:30px;background:#f7f7f7;border:1px solid #ccc;font-size:12px;letter-spacing:1px;color:#444;padding:8px 10px}
.promo{position:absolute;left:850px;top:67px;width:256px;height:146px;background:linear-gradient(#49b6e8,#1c87c5);border-radius:6px;overflow:hidden;box-shadow:0 6px 6px rgba(0,0,0,.2)}
.promo h3{position:absolute;left:66px;top:38px;font-family:"Roboto Condensed",Arial,sans-serif;font-weight:400;font-size:20px;color:var(--white)}
.promo p{position:absolute;left:66px;top:68px;width:180px;font-size:12px;line-height:20px;color:var(--white)}
.promo u{position:absolute;left:66px;top:118px;font-size:12px;color:var(--white)}
.ribbon{position:absolute;left:-30px;top:28px;width:130px;height:26px;background:#b3151c;transform:rotate(-45deg);color:var(--white);font-size:11px;text-align:center;line-height:26px}
.pager{position:absolute;top:218px;width:17px;height:17px;border-radius:50%;background:#999}
.bottom{left:0;top:1145px;width:1200px;height:37px;background:#fafafa;text-align:center;font-size:12px;letter-spacing:1px;color:#888;line-height:37px}
</style>
</head>
<body>

<header>
  <div class="abs brand">
    <span class="brand-name">vartelux</span>
    <span class="brand-tag">serious web developement</span>
  </div>
  <div class="abs social" aria-label="Social links"><span></span><span></span><span></span></div>
  <nav class="abs nav">
    <a href="#">Home</a><a href="#">About Us</a><a href="#">Services</a><a href="#">Addons</a><a href="#">Contact</a><a href="#">Blog</a>
  </nav>
</header>

<aside class="abs sidebar">
  <div class="search">Search here....
    <svg width="26" height="24" viewBox="0 0 26 24"><circle cx="9" cy="9" r="6.5" fill="none" stroke="#fff" stroke-width="3"/><line x1="14" y1="14" x2="23" y2="21" stroke="#fff" stroke-width="4" stroke-linecap="round"/></svg>
  </div>
  <div class="ads">
    <div class="ad">You can<b>Advertise</b><span class="here">HERE</span>▼</div>
    <div class="ad">You can<b>Advertise</b><span class="here">HERE</span>▼</div>
    <div class="ad">You can<b>Advertise</b><span class="here">HERE</span>▼</div>
    <div class="ad">You can<b>Advertise</b><span class="here">HERE</span>▼</div>
  </div>
  <div class="side-title" style="top:346px">Links Here</div>
  <ul class="links">
    <li class="active">Home</li><li>About Us</li><li>Services</li><li>Addons</li><li>Contact Us</li>
  </ul>
  <div class="side-title" style="top:524px">Subscribe</div>
  <div class="email">Enter email</div>
  <div class="btn-round" style="left:27px;top:621px">Subscribe</div>
</aside>

<main>
  <article class="abs post" style="top:149px">
    <h2 class="post-title">Lorem ipsum dolor sit amet, consectetur adipiscing elit. Mauris ut</h2>
    <p class="post-excerpt">Lorem Ipsum is simply dummy text of the printing and typesetting industry. Lorem Ipsum has been the industry's standard dummy text ever since the 1500s, when an unknown printer took a galley of type and scrambled it to make a type specimen book. It has survived</p>
    <div class="post-thumb" role="img" aria-label="Blog post illustration"></div>
    <div class="post-meta">Posted by <em>Vartelux</em> on Jan 3, 2012<span class="comments">0 comments</span><span class="more">Read more</span></div>
  </article>
  <article class="abs post" style="top:396px">
    <h2 class="post-title">Lorem ipsum dolor sit amet, consectetur adipiscing elit. Mauris ut</h2>
    <p class="post-excerpt">Lorem Ipsum is simply dummy text of the printing and typesetting industry. Lorem Ipsum has been the industry's standard dummy text ever since the 1500s, when an unknown printer took a galley of type and scrambled it to make a type specimen book. It has survived</p>
    <div class="post-thumb" role="img" aria-label="Blog post illustration"></div>
    <div class="post-meta">Posted by <em>Vartelux</em> on Jan 3, 2012<span class="comments">0 comments</span><span class="more">Read more</span></div>
  </article>
  <article class="abs post" style="top:644px">
    <h2 class="post-title">Lorem ipsum dolor sit amet, consectetur adipiscing elit. Mauris ut</h2>
    <p class="post-excerpt">Lorem Ipsum is simply dummy text of the printing and typesetting industry. Lorem Ipsum has been the industry's standard dummy text ever since the 1500s, when an unknown printer took a galley of type and scrambled it to make a type specimen book. It has survived</p>
    <div class="post-thumb" role="img" aria-label="Blog post illustration"></div>
    <div class="post-meta">Posted by <em>Vartelux</em> on Jan 3, 2012<span class="comments">0 comments</span><span class="more">Read more</span></div>
  </article>
</main>

<footer class="abs footer">
  <h3 class="col-title" style="left:85px">From Blog</h3>
  <div class="blog-item" style="top:56px"><a href="#">Quisque euismod orci...</a>Nulla luctus, purus in molestie posuere, lorem...</div>
  <div class="blog-item" style="top:143px"><a href="#">Quisque euismod orci...</a>Nulla luctus, purus in molestie posuere, lorem...</div>

  <h3 class="col-title" style="left:461px">Quick Contact</h3>
  <div class="field" style="top:61px">Name</div>
  <div class="field" style="top:97px">Email</div>
  <div class="field" style="top:133px;height:74px">Subject</div>
  <div class="btn-round" style="left:466px;top:215px">SUBMIT</div>

  <h3 class="col-title" style="left:839px">Quickstart Package</h3>
  <div class="promo">
    <div class="ribbon">ORDER NOW</div>
    <h3>Shopping Cart Hosting</h3>
    <p>Lorem ipsum dolor sit amet, consectetuer adipiscing elit,</p>
    <u>Learn more</u>
  </div>
  <span class="pager" style="left:1057px"></span><span class="pager" style="left:1082px"></span>
</footer>
<div class="abs bottom">Website content Copyrighted Vartelux 2012</div>

</body>
</html>
```